Owen Tasker Studios Business Card

Looking for a clear, modern, elegant, sharp business card that conveys a professional yet edgy image to my business as a wedding, portrait, and travel photographer. Would like something that looks vintage yet modern. Need a new business card to grow my business. We are growing the business for Wedding and Event Photography as well as fine art Photography. (Mostly Landscapes)
Updates

I’m looking through designs now but I have a new logo that i want using please.

New logo uploaded please redesign using that

PLEASE ALL DESIGNERS LOOK IN BRIEF FOR NEW LOGO

Target Market(s)

Brides, Grooms, Families with Kids, People looking for Fine Art Photography Artwork

Industry/Entity Type

Photographer

Contact Information for Business Card

Unsure

Font styles to use
Serif

Colors

Designer to choose colors to be used in the design.

Requirements
Must have
• My Website:
• http://taskerlens.examplefolio.net
• Phone:
• 323-481-5206
• Email:
• owentaskerlens@mailbox-example.net
Nice to have
• Would like a sort of shine on the printing finish.
• I like black I think it looks good on a business card.
• Can try working with my logo (png that I've attached)

```html
<!DOCTYPE html>
<html lang="en">
<head>
<meta charset="utf-8">
<title>Owen Tasker Studios — Business Card</title>
<link rel="stylesheet" href="https://fonts.googleapis.com/css2?family=Lato:wght@400;700&display=swap">
<style>
  :root {
    --bg: #1d1d1f;
    --card-edge: #0b0c0e;
    --frame-top: #1f2b3c;
    --frame-bottom: #0d0f10;
    --panel: #0a0b0d;
    --panel-light: #121418;
    --ink: #f4f4f4;
    --ink-soft: #e6e6e6;
    --icon-ink: #0b0c0e;
    --photo-sky: #3a5474;
    --photo-mid: #24354a;
    --photo-ground: #0e1210;
  }
  * { margin: 0; padding: 0; box-sizing: border-box; }
  html, body {
    width: 1200px;
    height: 1087px;
    overflow: hidden;
    background: var(--bg);
  }
  .canvas {
    position: relative;
    width: 1200px;
    height: 1087px;
    background: var(--bg);
    font-family: "Lato", sans-serif;
  }
  .card {
    position: absolute;
    left: 306px;
    width: 567px;
    height: 323px;
    background: var(--card-edge);
    box-shadow: 0 6px 18px rgba(0, 0, 0, 0.55);
    overflow: hidden;
  }
  .card--front { top: 204px; }
  .card--back { top: 573px; }

  .card__frame {
    position: absolute;
    inset: 0;
    background: linear-gradient(180deg, var(--frame-top) 0%, #141a22 45%, var(--frame-bottom) 100%);
  }
  .card--back .card__frame {
    background: linear-gradient(180deg, #08090b 0%, #0c0d0f 100%);
  }

  /* Front: contact panel */
  .contact-panel {
    position: absolute;
    left: 22px;
    top: 20px;
    width: 523px;
    height: 283px;
    background: linear-gradient(160deg, var(--panel-light) 0%, var(--panel) 60%, #08090a 100%);
  }
  .studio-name {
    position: absolute;
    left: 32px;
    top: 42px;
    font-weight: 700;
    font-size: 26px;
    letter-spacing: 2.2px;
    color: var(--ink);
    text-transform: uppercase;
    white-space: nowrap;
  }
  .contact-list {
    position: absolute;
    left: 32px;
    top: 104px;
    list-style: none;
  }
  .contact-item {
    display: flex;
    align-items: center;
    height: 32px;
    margin-bottom: 18px;
  }
  .contact-icon {
    width: 32px;
    height: 32px;
    border-radius: 50%;
    background: var(--ink);
    display: flex;
    align-items: center;
    justify-content: center;
    margin-right: 17px;
    flex: none;
  }
  .contact-icon svg { width: 18px; height: 18px; }
  .contact-text {
    font-weight: 400;
    font-size: 19px;
    color: var(--ink-soft);
    white-space: nowrap;
  }

  /* Back: photo with studio name */
  .photo-area {
    position: absolute;
    left: 22px;
    top: 20px;
    width: 523px;
    height: 283px;
    background:
      radial-gradient(ellipse at 70% 25%, rgba(70, 100, 135, 0.55) 0%, rgba(0, 0, 0, 0) 60%),
      linear-gradient(180deg, var(--photo-sky) 0%, var(--photo-mid) 55%, var(--photo-ground) 100%);
  }
  .brand-name {
    position: absolute;
    left: 0;
    right: 0;
    top: 138px;
    text-align: center;
    color: var(--ink);
    font-weight: 400;
    font-size: 28px;
    line-height: 1;
    white-space: nowrap;
  }
</style>
</head>
<body>
<main class="canvas">

  <section class="card card--front" aria-label="Business card front">
    <div class="card__frame"></div>
    <div class="contact-panel">
      <h1 class="studio-name">Owen Tasker Studios</h1>
      <ul class="contact-list">
        <li class="contact-item">
          <span class="contact-icon" aria-hidden="true">
            <svg viewBox="0 0 24 24"><path fill="var(--icon-ink)" d="M6.6 10.8c1.4 2.8 3.8 5.1 6.6 6.6l2.2-2.2c.3-.3.7-.4 1-.2 1.1.4 2.3.6 3.6.6.6 0 1 .4 1 1V20c0 .6-.4 1-1 1C10.6 21 3 13.4 3 4c0-.6.4-1 1-1h3.5c.6 0 1 .4 1 1 0 1.3.2 2.5.6 3.6.1.3 0 .7-.2 1l-2.3 2.2z"/></svg>
          </span>
          <span class="contact-text">323-481-5206</span>
        </li>
        <li class="contact-item">
          <span class="contact-icon" aria-hidden="true">
            <svg viewBox="0 0 24 24"><rect x="3.5" y="6" width="17" height="12" rx="1.2" fill="none" stroke="var(--icon-ink)" stroke-width="2"/><path d="M4 7l8 6 8-6" fill="none" stroke="var(--icon-ink)" stroke-width="2"/></svg>
          </span>
          <span class="contact-text">owentaskerlens@mailbox-example.net</span>
        </li>
        <li class="contact-item">
          <span class="contact-icon" aria-hidden="true">
            <svg viewBox="0 0 24 24"><circle cx="12" cy="12" r="8.5" fill="var(--icon-ink)"/><path d="M8 8.5c1.5-.3 2.5.6 2.2 1.8-.3 1-1.8 1-1.6 2.3.2 1 1.4 1.3 1.3 2.6M14 5.5c-.4 1.3.5 2 1.5 2.2 1.2.2 1.6 1.3 1 2.3M13.5 14c1-.6 2.4-.2 2.7 1" fill="none" stroke="var(--ink)" stroke-width="1.3" stroke-linecap="round"/></svg>
          </span>
          <span class="contact-text">taskerlens.examplefolio.net</span>
        </li>
      </ul>
    </div>
  </section>

  <section class="card card--back" aria-label="Business card back">
    <div class="card__frame"></div>
    <div class="photo-area" role="img" aria-label="Dusk wedding photograph: silhouetted couple beside a bunch of balloons against a deep blue evening sky"></div>
    <p class="brand-name">Owen Tasker Studios</p>
  </section>

</main>
</body>
</html>
```